Halvor Interiors Studio New Business Card

I am opening a new division of my business. I am a high end interior designer, and the new business is writing specs for construction projects. It will be marketed to the VERY high end contractor, architects and realtors. The client will actually be the one who pays us and signs the agreement, but it will be the contractor, architect or realtor that will recommend us. I have attached my current card and our previous logo which is still used on some of our paperwork. I would like the new logo to be connected in some way to what we are currently using. We will need to have room on the card for a person's name. I'd like to omit the address as we might be moving the office soon. The web address is www.HalvorInteriorsStudio.example. For this design, please use my name, Marisol Fenwick.

Target Market(s)

High End Luxury Contractors, Realtors and Architects

Industry/Entity Type

Residential Construction

Contact Information for Business Card

Halvor Interiors Studio, Phone: 555-204-9167, www.HalvorInteriorsStudio.example , Marisol Fenwick

Font styles to use
Sans Serif

Colors
ec1f27

Requirements
Must have
• Some visual reference to my current card and logos. Use the colors submitted on the business card I attached.
Nice to have
• A visual reference to my current card and logos. Use the colors submitted on the card I attached.
Should not have
• A physical address

```html
<!DOCTYPE html>
<html lang="en">
<head>
<meta charset="utf-8">
<title>Halvor Interiors Studio — Business Card</title>
<link rel="stylesheet" href="https://fonts.googleapis.com/css2?family=Josefin+Sans:wght@400;600&display=swap">
<style>
  :root {
    --backdrop: #e6e6e6;
    --card: #ffffff;
    --ink: #1f1f1f;
    --ink-soft: #6b6b6b;
    --accent: #ec1f27;
  }
  html, body {
    margin: 0;
    width: 1200px;
    height: 800px;
    overflow: hidden;
    background: var(--backdrop);
  }
  .card {
    position: absolute;
    left: 100px;
    top: 115px;
    width: 1000px;
    height: 570px;
    background: var(--card);
    font-family: "Josefin Sans", sans-serif;
    color: var(--ink);
    box-shadow: 0 2px 10px rgba(0,0,0,0.08);
  }
  .identity {
    position: absolute;
    right: 540px;
    top: 228px;
    width: 420px;
    text-align: right;
  }
  .identity__accent {
    position: absolute;
    right: 50px;
    top: -16px;
    width: 220px;
    height: 3px;
    background: var(--accent);
  }
  .identity__person {
    margin: 0;
    font-size: 50px;
    font-weight: 600;
    color: var(--ink-soft);
    line-height: 1;
    white-space: nowrap;
  }
  .identity__tagline {
    margin: 4px 0 0;
    font-size: 11px;
    letter-spacing: 3.6px;
    color: var(--ink-soft);
    white-space: nowrap;
  }
  .identity__company {
    margin: 6px 0 0;
    font-size: 25px;
    font-weight: 400;
    letter-spacing: 0.3px;
    text-transform: uppercase;
    color: var(--ink);
    white-space: nowrap;
  }
  .brace {
    position: absolute;
    left: 475px;
    top: 183px;
    width: 90px;
    height: 205px;
  }
  .contact {
    position: absolute;
    left: 580px;
    top: 218px;
    margin: 0;
    padding: 0;
    list-style: none;
  }
  .contact__item {
    display: flex;
    align-items: center;
    height: 34px;
    margin-bottom: 30px;
    font-size: 20px;
    letter-spacing: 0.5px;
    white-space: nowrap;
  }
  .contact__icon {
    width: 24px;
    height: 24px;
    margin-right: 30px;
    flex: none;
  }
</style>
</head>
<body>
  <main class="card">
    <section class="identity">
      <span class="identity__accent" aria-hidden="true"></span>
      <h1 class="identity__person">Marisol Fenwick</h1>
      <p class="identity__tagline">COMMERCIAL | RESIDENTIAL DESIGN</p>
      <p class="identity__company">Halvor Interiors Studio</p>
    </section>

    <svg class="brace" viewBox="0 0 90 205" aria-hidden="true">
      <path fill="var(--ink)" d="M88 2 C55 6 42 22 42 52 L42 78 C42 92 32 100 4 102.5 C32 105 42 113 42 127 L42 153 C42 183 55 199 88 203 L88 199 C64 194 54 180 54 153 L54 127 C54 112 44 105 24 102.5 C44 100 54 93 54 78 L54 52 C54 25 64 11 88 6 Z"/>
    </svg>

    <ul class="contact">
      <li class="contact__item">
        <svg class="contact__icon" viewBox="0 0 24 24" aria-hidden="true">
          <rect x="6" y="2" width="12" height="20" rx="2" fill="none" stroke="var(--ink)" stroke-width="2"/>
          <rect x="8.5" y="5" width="7" height="11" fill="var(--ink)"/>
        </svg>
        <span>555-204-9167</span>
      </li>
      <li class="contact__item">
        <svg class="contact__icon" viewBox="0 0 24 24" aria-hidden="true">
          <g fill="none" stroke="var(--ink)" stroke-width="1.6">
            <circle cx="12" cy="12" r="10"/>
            <ellipse cx="12" cy="12" rx="4.5" ry="10"/>
            <line x1="2" y1="12" x2="22" y2="12"/>
            <path d="M4 7 H20 M4 17 H20"/>
          </g>
        </svg>
        <span>www.HalvorInteriorsStudio.example</span>
      </li>
    </ul>
  </main>
</body>
</html>
```